Our Velvetline

I am developing a web site which sells preowned high end designer handbags and accessories. Some of the brands include: Duvore, Marcel Ostrand & Velka, to name a few. I am after a luxurious and high end feel.

Some brands I like that express this feel include: Corvin, Velka, thecloset-kip.com, pursetradeorloan.com

I am after a logo, business card, letterhead, with compliments, address label and envelope designs.
The business name is Our velvetline, and the website will be www.ourvelvetline.com.au. I have thoughts of using OVL as a logo or OUR velvetline.com.au

I don't want a large logo, it needs to blend in with the name in some way - or may not need an image at all, if the style of the font speaks to the brand.

Thank-you

Reason: I would like to give designers plenty of time to be able to submit a design.

Target Market(s)

Women, aged 25-60 who are into fashion

Industry/Entity Type

Business

Requirements
Must have
• High End
Luxurious

```html
<!DOCTYPE html>
<html lang="en">
<head>
<meta charset="utf-8">
<title>Our Velvetline — Stationery Set</title>
<link rel="stylesheet" href="https://fonts.googleapis.com/css2?family=Questrial&family=Tinos:wght@400;700&display=swap">
<style>
  :root {
    --slate: #4b5683;
    --slate-light: #67719c;
    --slate-deep: #3e4874;
    --paper: #ffffff;
    --ink-soft: #a3a6b0;
    --ink-mid: #8d909a;
    --ghost: #e2e3e6;
    --backdrop: #eceae6;
  }
  * { box-sizing: border-box; margin: 0; padding: 0; }
  html, body { width: 1200px; height: 840px; overflow: hidden; background: var(--backdrop); }
  .canvas { position: relative; width: 1200px; height: 840px; font-family: "Questrial", "Helvetica Neue", sans-serif; }

  .brand { font-family: "Questrial", sans-serif; font-weight: 400; letter-spacing: 1px; line-height: 1; }

  /* Letterhead */
  .letterhead { position: absolute; left: 44px; top: 50px; width: 571px; height: 743px; background: var(--paper); overflow: hidden; }
  .letterhead-top { position: absolute; left: 0; top: 0; width: 571px; height: 110px; }
  .letterhead-logo { position: absolute; left: 28px; top: 16px; font-size: 36px; color: var(--paper); }
  .letterhead-divider { position: absolute; left: 458px; top: 8px; width: 1px; height: 76px; background: rgba(255,255,255,.55); }
  .letterhead-info { position: absolute; left: 470px; top: 14px; font-size: 22px; line-height: 22px; color: rgba(255,255,255,.7); letter-spacing: .5px; }
  .letter { position: absolute; left: 96px; top: 128px; width: 420px; font-family: "Tinos", "Times New Roman", serif; font-size: 7.5px; line-height: 11px; color: var(--ink-soft); }
  .letter p { margin-bottom: 11px; }
  .letter .body-copy { color: #b3b6bf; }
  .letter .signature { margin-top: 33px; }
  .letterhead-bottom { position: absolute; left: 0; bottom: 0; width: 571px; height: 118px; }
  .letterhead-url { position: absolute; left: 0; right: 0; bottom: 14px; text-align: center; font-size: 13px; letter-spacing: 1.5px; color: rgba(255,255,255,.85); }

  /* Business cards */
  .card { position: absolute; top: 40px; width: 250px; height: 143px; overflow: hidden; }
  .card-back { left: 652px; background: linear-gradient(180deg, var(--slate) 0%, var(--slate-light) 100%); }
  .card-back .brand { position: absolute; left: 0; right: 0; top: 44px; text-align: center; font-size: 36px; color: var(--paper); }
  .card-back .card-rule { position: absolute; left: 72px; width: 106px; top: 84px; height: 1px; background: rgba(255,255,255,.8); }
  .card-back .card-url { position: absolute; left: 0; right: 0; top: 88px; text-align: center; font-size: 7.5px; color: var(--paper); letter-spacing: .3px; }

  .card-front { left: 918px; background: var(--paper); }
  .card-front-panel { position: absolute; left: 0; top: 0; width: 112px; height: 143px; background: linear-gradient(180deg, var(--slate) 0%, var(--slate-light) 100%); }
  .card-front-stripe { position: absolute; left: 118px; top: 0; width: 5px; height: 143px; background: var(--slate); }
  .card-front .brand { position: absolute; left: 10px; top: 52px; font-size: 26px; color: var(--paper); }
  .card-front .card-rule { position: absolute; left: 10px; top: 80px; width: 88px; height: 1px; background: rgba(255,255,255,.8); }
  .card-front .card-url { position: absolute; left: 10px; top: 83px; font-size: 6px; color: var(--paper); }
  .card-ghost-mark { position: absolute; left: 134px; top: 10px; font-size: 52px; color: var(--ghost); }
  .card-holder { position: absolute; left: 146px; top: 88px; color: var(--slate-deep); }
  .card-holder-name { font-size: 10px; letter-spacing: .8px; margin-bottom: 3px; }
  .card-holder-detail { font-size: 6.5px; line-height: 8px; }

  /* Envelopes */
  .envelope { position: absolute; left: 652px; width: 516px; height: 222px; background: var(--paper); overflow: hidden; }
  .envelope-back { top: 226px; }
  .envelope-flap { position: absolute; left: 0; top: 0; width: 516px; height: 92px; }
  .envelope-back .brand { position: absolute; left: 0; right: 0; top: 24px; text-align: center; font-size: 36px; color: var(--paper); }
  .envelope-back-band { position: absolute; left: 0; right: 0; bottom: 0; height: 18px; background: var(--slate); }

  .envelope-front { top: 574px; border: 1px solid #d8d9dd; }
  .envelope-front .brand { position: absolute; left: 22px; top: 22px; font-size: 32px; color: var(--slate); }
  .envelope-front .envelope-rule { position: absolute; left: 22px; top: 56px; width: 110px; height: 1px; background: var(--slate); }
  .envelope-front .envelope-url { position: absolute; left: 22px; top: 59px; font-size: 7.5px; color: var(--slate-deep); }
  .envelope-front-band { position: absolute; left: 0; right: 0; bottom: 0; height: 34px; background: linear-gradient(180deg, var(--slate) 0%, var(--slate-light) 100%); }
</style>
</head>
<body>
<main class="canvas">

  <section class="letterhead" aria-label="Letterhead">
    <svg class="letterhead-top" viewBox="0 0 571 110" aria-hidden="true">
      <defs>
        <linearGradient id="band-top" x1="0" y1="0" x2="0" y2="1">
          <stop offset="0" stop-color="#4b5683"/>
          <stop offset="1" stop-color="#67719c"/>
        </linearGradient>
      </defs>
      <path d="M0 0 H571 V62 C470 64 360 82 250 80 C150 78 70 64 0 58 Z" fill="url(#band-top)"/>
      <path d="M0 76 C80 84 170 94 260 94 C370 94 470 78 571 72 V80 C470 86 370 102 260 102 C170 102 80 92 0 84 Z" fill="#4b5683"/>
    </svg>
    <div class="letterhead-logo brand">OVL</div>
    <div class="letterhead-divider"></div>
    <div class="letterhead-info">INFO<br>HERE</div>

    <article class="letter">
      <p>May 13th 2011</p>
      <p>Recipient's name<br>Adress<br>City, State, Zip code</p>
      <p>Dear Recipient</p>
      <p class="body-copy">Thank you for your recent interest in our collection of preowned designer handbags and accessories. Every piece is inspected by hand, authenticated and cleaned before it is listed, so you can shop with full confidence in what arrives at your door.</p>
      <p class="body-copy">We source from private owners across the country and work only with pieces in excellent condition. Each listing includes clear notes on wear, original packaging and care, so there are no surprises.</p>
      <p class="body-copy">Our team is happy to help you find a particular style, colour or size. Send us a short note with what you have in mind and we will let you know as soon as a matching piece becomes available in the store. We can also hold an item for a short time while you decide.</p>
      <p class="body-copy">Should you wish to sell a bag of your own, we offer a simple consignment service with fair pricing and careful presentation. Please contact us for details.</p>
      <p>Yours Sincerely</p>
      <p class="signature">Daniel Hart<br>CEO</p>
    </article>

    <svg class="letterhead-bottom" viewBox="0 0 571 118" aria-hidden="true">
      <defs>
        <linearGradient id="band-bottom" x1="0" y1="0" x2="0" y2="1">
          <stop offset="0" stop-color="#5a6490"/>
          <stop offset="1" stop-color="#4b5683"/>
        </linearGradient>
      </defs>
      <path d="M0 12 C120 2 230 6 330 22 C430 38 510 30 571 24 V118 H0 Z" fill="url(#band-bottom)"/>
    </svg>
    <div class="letterhead-url">www.ourvelvetline.com.au</div>
  </section>

  <section class="card card-back" aria-label="Business card, back">
    <div class="brand">OVL</div>
    <div class="card-rule"></div>
    <div class="card-url">www.ourvelvetline.com.au</div>
  </section>

  <section class="card card-front" aria-label="Business card, front">
    <div class="card-front-panel"></div>
    <div class="card-front-stripe"></div>
    <div class="brand">OVL</div>
    <div class="card-rule"></div>
    <div class="card-url">www.ourvelvetline.com.au</div>
    <div class="card-ghost-mark brand">OVL</div>
    <div class="card-holder">
      <div class="card-holder-name">YOUR NAME HERE</div>
      <div class="card-holder-detail">Director<br>Contact Number<br>Information</div>
    </div>
  </section>

  <section class="envelope envelope-back" aria-label="Envelope, back">
    <svg class="envelope-flap" viewBox="0 0 516 92" aria-hidden="true">
      <defs>
        <linearGradient id="flap" x1="0" y1="0" x2="0" y2="1">
          <stop offset="0" stop-color="#5e6893"/>
          <stop offset="1" stop-color="#4b5683"/>
        </linearGradient>
      </defs>
      <path d="M0 0 H516 V28 C440 40 380 86 258 88 C136 86 76 40 0 28 Z" fill="url(#flap)"/>
    </svg>
    <div class="brand">OVL</div>
    <div class="envelope-back-band"></div>
  </section>

  <section class="envelope envelope-front" aria-label="Envelope, front">
    <div class="brand">OVL</div>
    <div class="envelope-rule"></div>
    <div class="envelope-url">www.ourvelvetline.com.au</div>
    <div class="envelope-front-band"></div>
  </section>

</main>
</body>
</html>
```